Revamp our wedding venue website

Currently we are using wordpress for our website and hoped to find a designer that can assist us with making the website prettier and more pleasing and draw more interest. www.velmarhall.com is our current site. We are connected to google business mail, so I would prefer to stay with this for now and update our gallery with new photos, blog page and putting the contact us form back on all the pages.

Target Market(s)

20-40 years of age, all ranges of styles and generally clients looking for a different modern feel vs. a hotel hall.

Industry/Entity Type

Wedding

Logo Text

1927 Velmar Hall

Number of Pages Required

4 page

Font styles to use
Serif

Requirements
Must have
• Light, airy feel. Romantic and informative. Mobile friendly and easy to contact us-preferred contact form on all pages. Gallery of photos. Previous reviews
Nice to have
• Bio of staff, maybe some videos, and fun things to do in the area for out of town guests. Maps and also venue blank floor plan.

```html
<!DOCTYPE html>
<html lang="en">
<head>
<meta charset="utf-8">
<title>1927 Velmar Hall</title>
<link href="https://fonts.googleapis.com/css2?family=Bree+Serif&family=Dancing+Script:wght@500&family=Josefin+Sans:wght@400;600&display=swap" rel="stylesheet">
<style>
:root{
  --sand:#d9cdbb;
  --brown:#5b4a3f;
  --brown-dark:#3d3029;
  --ink:#2b2522;
  --muted:#5f5852;
  --white:#ffffff;
  --purple:#2a1538;
  --night:#141414;
  --mist:#ececec;
  --line:#9a9a9a;
}
*{box-sizing:border-box;margin:0;padding:0}
html,body{width:1200px;height:2835px;overflow:hidden}
body{font-family:"Josefin Sans",sans-serif;color:var(--ink);background:var(--white);position:relative}
.section{position:absolute;left:0;width:1200px}
.script{font-family:"Dancing Script",cursive;font-weight:500}
.serif{font-family:"Bree Serif",serif}

/* header */
.topbar{top:0;height:93px;background:var(--sand)}
.social{position:absolute;display:flex;gap:8px}
.social span{width:24px;height:24px;border-radius:50%;background:var(--white);display:block}
.topbar .social{left:160px;top:32px}
.brand{position:absolute;left:0;right:0;top:8px;text-align:center;color:var(--ink);font-size:34px;line-height:38px}
.brand small{display:block;font-size:30px;line-height:36px}
.top-contact{position:absolute;left:880px;top:20px;font-size:15px;line-height:30px;color:var(--ink)}
.top-contact div{display:flex;align-items:center;gap:12px}
.nav{top:93px;height:39px;background:var(--brown);display:flex;align-items:center;justify-content:center;gap:18px}
.nav a{color:var(--white);text-decoration:none;font-family:"Bree Serif",serif;font-size:12px;letter-spacing:.5px}
.nav i{color:#e6dccd;font-style:normal;font-size:12px}

/* hero */
.hero{top:132px;height:486px;background:linear-gradient(100deg,#8a0f14 0%,#c5141c 25%,#3a0b10 45%,#d7262b 70%,#7a0a10 100%)}
.hero-caption{position:absolute;left:0;bottom:0;width:100%;height:68px;background:rgba(20,14,12,.55);color:var(--white);padding:10px 0 0 162px;font-family:"Bree Serif",serif;font-size:22px;line-height:26px}
.dots{position:absolute;right:160px;bottom:28px;display:flex;gap:6px}
.dots span{width:11px;height:11px;border-radius:50%;border:1px solid #aaa}
.dots .on{background:#aaa}

/* welcome */
.welcome{top:618px;height:308px}
.welcome h1{position:absolute;left:162px;top:42px;font-size:38px;font-weight:500;color:var(--ink);line-height:44px}
.welcome h1:after{content:"";position:absolute;left:0;bottom:-4px;width:420px;height:1px;background:#bbb}
.welcome-text{position:absolute;left:162px;top:100px;width:570px}
.welcome-text p{font-size:12px;line-height:23px;color:var(--muted)}
.btn{position:absolute;background:var(--brown);color:var(--white);font-family:"Bree Serif",serif;font-size:12px;text-align:center}
.welcome .btn{position:static;display:inline-block;margin-top:12px;width:94px;height:28px;line-height:28px}
.welcome .photo{position:absolute;left:746px;top:64px;width:294px;height:186px;border:3px solid var(--brown);background:linear-gradient(180deg,#5f8fd1 0%,#9ac0ea 40%,#b2622c 45%,#8a4a22 100%)}

/* shared title */
.title{position:absolute;left:0;width:100%;text-align:center;font-size:40px}
.divider{position:absolute;left:450px;width:300px;height:30px}
.divider:before{content:"";position:absolute;left:0;right:0;top:15px;height:1px;background:var(--line)}
.divider .badge{position:absolute;left:136px;top:0;width:30px;height:30px;border-radius:50%;display:flex;align-items:center;justify-content:center}

/* events */
.events{top:926px;height:428px;background:linear-gradient(180deg,#2d1540,#1b0d26 60%,#120a18);color:var(--white)}
.events .title{top:38px}
.events .badge,.blog .badge{background:var(--white)}
.cards{position:absolute;left:162px;display:flex;gap:46px}
.card{width:262px;text-align:center}
.card .img{height:115px;border:3px solid var(--white)}
.card h3{font-family:"Bree Serif",serif;font-weight:400;font-size:20px;margin-top:24px}
.card p{font-size:11.5px;line-height:18px;margin-top:10px;padding:0 6px}
.events .cards{top:166px}

/* gallery */
.gallery{top:1354px;height:588px;background:var(--white)}
.gallery .title{top:58px;color:var(--ink)}
.gallery .badge,.contact .badge{background:var(--ink)}
.grid{position:absolute;left:162px;top:146px;width:878px;height:372px;background:#f4f4f4;padding:8px 16px}
.tile{position:absolute;border:2px solid #ddd}
.zoom{display:flex;align-items:center;justify-content:center;border:3px solid var(--ink)}

/* blog */
.blog{top:1942px;height:448px;background:linear-gradient(180deg,#1c1a18,#0d0c0b);color:var(--white)}
.blog .title{top:36px}
.blog .cards{top:150px}
.post{position:relative}
.post .img{height:106px;border:2px solid #ccc}
.date{position:absolute;left:4px;top:4px;background:var(--white);color:var(--ink);font-family:"Bree Serif",serif;font-size:12px;line-height:13px;padding:2px 6px;text-align:left}
.post h3{margin-top:22px;font-size:19px}
.post p{margin-top:6px;font-size:11.5px;line-height:16px}
.post .rule{margin:20px auto 0;width:230px;height:1px;background:#aaa;position:relative}
.post .rule span{position:absolute;left:108px;top:-7px;width:14px;height:14px;background:var(--white);color:var(--ink);font-size:13px;line-height:14px;font-weight:600}

/* contact */
.contact{top:2390px;height:390px;background:linear-gradient(160deg,#f4f4f4,#e2e2e2 50%,#f0f0f0)}
.contact .title{top:38px}
.contact h4{position:absolute;font-family:"Bree Serif",serif;font-weight:400;font-size:15px}
.field{position:absolute;background:var(--white);border:1px solid #ddd;font-size:10px;color:#666;padding:8px 10px}
.info{position:absolute;left:860px;top:210px;font-size:11px;line-height:16px;color:#555}
.info .row{display:flex;align-items:center;gap:8px;margin-top:12px}
.footer{top:2780px;height:55px;background:var(--night);color:#ccc;font-size:12px}
.footer .copy{position:absolute;left:162px;top:22px}
.footer .social{left:920px;top:16px}
.footer .social span{background:var(--white)}
</style>
</head>
<body>

<header class="section topbar">
  <div class="social"><span></span><span></span><span></span><span></span></div>
  <div class="brand script">1927<small>Velmar Hall</small></div>
  <div class="top-contact">
    <div><svg width="14" height="14" viewBox="0 0 24 24"><path fill="#3d3029" d="M6.6 10.8a15 15 0 006.6 6.6l2.2-2.2c.3-.3.7-.4 1-.2 1.1.4 2.3.6 3.6.6.6 0 1 .4 1 1V20c0 .6-.4 1-1 1C10.6 21 3 13.4 3 4c0-.6.4-1 1-1h3.5c.6 0 1 .4 1 1 0 1.3.2 2.5.6 3.6.1.3 0 .7-.2 1z"/></svg>555-0142-870</div>
    <div><svg width="14" height="12" viewBox="0 0 24 20"><path fill="#3d3029" d="M2 2h20v16H2z"/><path fill="none" stroke="#d9cdbb" stroke-width="2" d="M2 3l10 8 10-8"/></svg>events@velmarhall.com</div>
  </div>
</header>

<nav class="section nav">
  <i>✻</i><a>HOME</a><i>✻</i><a>WEDDING</a><i>✻</i><a>EVENTS</a><i>✻</i><a>CATERING</a><i>✻</i><a>GALLERY</a><i>✻</i><a>BLOG</a><i>✻</i><a>CONTACT US</a><i>✻</i>
</nav>

<section class="section hero" role="img" aria-label="Reception hall set with white-draped tables, silver chairs, red uplighting and a tiered wedding cake">
  <div class="hero-caption">"Imagine Your Wedding Or Event In Harbor City's Premiere,<br>Unique And Historic Venue"</div>
  <div class="dots"><span></span><span class="on"></span><span></span><span></span></div>
</section>

<section class="section welcome">
  <h1 class="script">Welcome To 1927 Velmar Hall</h1>
  <div class="welcome-text">
    <p>Lorem ipsum dolor sit amet, consectetur adipiscing elit, sed do eiusmod tempor incididunt ut labore et dolor magna aliqua. Ut enim ad minim veniam, quis nostrud exercitation ullamco laboris nisi ut aliquip ex ea commod consequat Duis aute irure dolor in reprehenderit in voluptate velit esse cillum dolore eu fugiat nulla pariatur. Except occaecat non proident, sunt in culpa quid consequat non proident, sunt in culpa quid cuis aute irure dolor in repproeserunt mollit anim id est laborum.</p>
    <div class="btn">Read More</div>
  </div>
  <div class="photo" role="img" aria-label="Brick venue building exterior under blue sky"></div>
</section>

<section class="section events">
  <h2 class="title script">Our Events</h2>
  <div class="divider" style="top:98px"><div class="badge"><svg width="16" height="16" viewBox="0 0 16 16"><rect x="2" y="3" width="12" height="11" fill="none" stroke="#222" stroke-width="1.6"/><path d="M2 6h12M5 1v3M11 1v3" stroke="#222" stroke-width="1.6"/></svg></div></div>
  <div class="cards">
    <div class="card"><div class="img" role="img" aria-label="Conference table with water bottles" style="background:linear-gradient(90deg,#1c2630,#7a8790,#d9c9a6,#40525f)"></div><h3>Corporate Events</h3><p>The Velmar Hall is the perfect venue for your next professional event. Out of the ever-present stuffy meeting rooms...[ + ]</p></div>
    <div class="card"><div class="img" role="img" aria-label="Guests raising champagne glasses in a toast" style="background:linear-gradient(90deg,#d9c7a8,#f3ecdf,#c9a67a,#e7dccb)"></div><h3>Private Events</h3><p>Private events include special Bar/Bat Mitzvah, Quinceañera, Confirmation Party, Birthday celebration,family reunion, or...[ + ]</p></div>
    <div class="card"><div class="img" role="img" aria-label="Crowd with raised hands at a concert" style="background:linear-gradient(90deg,#3a2410,#c99a45,#6b4518,#e2b760)"></div><h3>Public Events</h3><p>Think of the Velmar Hall when you need to promote, host or organize a public function. Our great location and unique...[ + ]</p></div>
  </div>
</section>

<section class="section gallery">
  <h2 class="title script">Our Photo Gallery</h2>
  <div class="divider" style="top:112px;left:424px;width:352px"><div class="badge" style="left:162px"><svg width="16" height="14" viewBox="0 0 16 14"><path fill="#fff" d="M1 4h3l1.5-2h5L12 4h3v9H1z"/><circle cx="8" cy="8.5" r="2.6" fill="#222"/></svg></div></div>
  <div class="grid">
    <div class="tile" role="img" aria-label="Long dining table with hanging yellow decorations" style="left:16px;top:8px;width:272px;height:164px;background:linear-gradient(180deg,#c9c1a0,#a9a27c 60%,#e3e0d5)"></div>
    <div class="tile" role="img" aria-label="Server pouring drinks into glasses" style="left:302px;top:8px;width:272px;height:164px;background:linear-gradient(135deg,#5a4a3a,#e6dccb 40%,#f5f1ea 70%,#c8b38f)"></div>
    <div class="tile" role="img" aria-label="Plated appetizers and glasses on a buffet" style="left:590px;top:8px;width:272px;height:344px;background:linear-gradient(160deg,#2a2622,#e8e2d6 35%,#8a6a48 60%,#f0ebe2 85%,#3a302a)"></div>
    <div class="tile" role="img" aria-label="Rows of red and blue layered shots" style="left:16px;top:188px;width:272px;height:164px;background:linear-gradient(180deg,#c9ccd6,#2b4db0 35%,#c02a30 60%,#e6c59a)"></div>
    <div class="tile zoom" role="img" aria-label="Champagne glasses on a tray" style="left:302px;top:188px;width:272px;height:164px;background:linear-gradient(135deg,#d8d8d8,#c6c6c6)"><svg width="44" height="44" viewBox="0 0 44 44"><circle cx="18" cy="18" r="14" fill="none" stroke="#333" stroke-width="3"/><path d="M28 28l12 12M11 18h14M18 11v14" stroke="#333" stroke-width="3"/></svg></div>
  </div>
</section>

<section class="section blog">
  <h2 class="title script">Latest Blog</h2>
  <div class="divider" style="top:98px"><div class="badge"><svg width="14" height="12" viewBox="0 0 14 12"><path d="M0 1h3M5 1h9M0 6h3M5 6h9M0 11h3M5 11h9" stroke="#222" stroke-width="2"/></svg></div></div>
  <div class="cards">
    <div class="card post"><div class="img" role="img" aria-label="Lounge area with white furniture and purple lighting" style="background:linear-gradient(180deg,#c8c0b4,#6c5a7a 55%,#2a2430)"></div><div class="date">21<br>OCT</div><h3 class="serif">Duis Aueum Iriure Dolo</h3><p>Fillum dolore eu feugiat nulla facilisis at,<br>consectetuerlit, sedonumfacilisi...</p><div class="rule"><span>+</span></div></div>
    <div class="card post"><div class="img" role="img" aria-label="Bamboo and orchid floral arrangement" style="background:linear-gradient(90deg,#3d5a2a,#a7c06a,#b24fa6,#5e7d3a)"></div><div class="date">21<br>OCT</div><h3 class="serif">Duis Aueum Iriure Dolo</h3><p>Fillum dolore eu feugiat nulla facilisis at,<br>consectetuerlit, sedonumfacilisi...</p><div class="rule"><span>+</span></div></div>
    <div class="card post"><div class="img" role="img" aria-label="Bouquet of yellow and white flowers" style="background:radial-gradient(circle at 50% 50%,#f4cf2a,#e6a81e 45%,#f3efe2 75%,#6b8a4a)"></div><div class="date">21<br>OCT</div><h3 class="serif">Duis Aueum Iriure Dolo</h3><p>Fillum dolore eu feugiat nulla facilisis at,<br>consectetuerlit, sedonumfacilisi...</p><div class="rule"><span>+</span></div></div>
  </div>
</section>

<section class="section contact">
  <h2 class="title script">Contact</h2>
  <div class="divider" style="top:102px;left:474px;width:252px"><div class="badge" style="left:112px"><svg width="14" height="11" viewBox="0 0 24 20"><path fill="#fff" d="M2 2h20v16H2z"/><path fill="none" stroke="#222" stroke-width="2" d="M2 3l10 8 10-8"/></svg></div></div>
  <h4 style="left:162px;top:152px">And We Will Help You Shape Your Future</h4>
  <div style="position:absolute;left:162px;top:176px;width:36px;height:1px;background:#555"></div>
  <div class="field" style="left:162px;top:210px;width:232px;height:32px">Your Name</div>
  <div class="field" style="left:162px;top:256px;width:232px;height:32px">Your Email</div>
  <div class="field" style="left:162px;top:302px;width:232px;height:32px">Mobile No.</div>
  <div class="field" style="left:402px;top:210px;width:292px;height:80px">Your Message or Query</div>
  <div class="btn" style="left:402px;top:302px;width:292px;height:32px;line-height:32px">Send Us Your Informations</div>
  <h4 style="left:860px;top:152px">Contact Information</h4>
  <div style="position:absolute;left:860px;top:176px;width:76px;height:1px;background:#555"></div>
  <div class="info">
    VELMAR HALL<br>418 LINDEN ROW, HARBOR CITY, FL<br>30412
    <div class="row"><svg width="11" height="11" viewBox="0 0 24 24"><path fill="#444" d="M6.6 10.8a15 15 0 006.6 6.6l2.2-2.2c.3-.3.7-.4 1-.2 1.1.4 2.3.6 3.6.6.6 0 1 .4 1 1V20c0 .6-.4 1-1 1C10.6 21 3 13.4 3 4c0-.6.4-1 1-1h3.5c.6 0 1 .4 1 1 0 1.3.2 2.5.6 3.6.1.3 0 .7-.2 1z"/></svg>555-0142-870</div>
    <div class="row"><svg width="11" height="11" viewBox="0 0 24 24"><path fill="#444" d="M6 2h12v6H6zM3 9h18v9h-3v4H6v-4H3z"/></svg>555-0142-870</div>
    <div class="row"><svg width="11" height="9" viewBox="0 0 24 20"><path fill="#444" d="M2 2h20v16H2z"/><path fill="none" stroke="#eee" stroke-width="2" d="M2 3l10 8 10-8"/></svg>events@velmarhall.com</div>
  </div>
</section>

<footer class="section footer">
  <div class="copy">Copyright © 2016 VELMAR HALL, All Rights Reserved.</div>
  <div class="social"><span></span><span></span><span></span><span></span></div>
</footer>

</body>
</html>
```